Become a Mentor - For Musicians, Artists, Producers and Teachers

Here is the full creative brief:

https://files.plenwick.com/sheets/d/4kTqpLm8Wz_2RNa7Hc3Xv91Jd0Gb5YeUsQ6fNo8rTpxa/view?mode=shared

Here is the background image file: https://www.trovecrate.com/sh/83jbwtrmq5dkx2u/BBHn4k7QTf2ZpLeXX-wr9MUHe?dl=0

LOGO:
https://www.trovecrate.com/sh/k472rufmpdo9b6w/BBKLe3RtHY5J-sFQnLZw7Ggma?dl=0

```html
<!DOCTYPE html>
<html lang="en">
<head>
<meta charset="UTF-8">
<title>Become a Mentor – Meridian School of Music</title>
<link rel="stylesheet" href="https://fonts.googleapis.com/css2?family=Cinzel:wght@700;900&family=Roboto:ital,wght@0,400;0,500;1,300&display=swap">
<style>
  :root {
    --page: #ffffff;
    --ink: #ffffff;
    --panel-core: #0b4ea3;
    --panel-mid: #1a2e7a;
    --panel-deep: #26104a;
    --accent-wave: #1f4c82;
    --accent-corner: #17427c;
    --photo-a: #3b3a3f;
    --photo-b: #6a5a4e;
    --photo-c: #1f1d22;
  }
  * { margin: 0; padding: 0; box-sizing: border-box; }
  html, body { width: 1200px; height: 1000px; overflow: hidden; background: var(--page); }
  .poster {
    position: absolute; left: 271px; top: 34px;
    width: 658px; height: 933px; overflow: hidden;
    background: radial-gradient(ellipse 520px 420px at 300px 560px, var(--panel-core) 0%, var(--panel-mid) 55%, var(--panel-deep) 100%);
    font-family: "Roboto", sans-serif; color: var(--ink);
  }
  .hero-photo {
    position: absolute; left: 0; top: 0; width: 658px; height: 466px;
    background: linear-gradient(120deg, var(--photo-a) 0%, var(--photo-b) 45%, var(--photo-c) 100%);
  }
  .shapes { position: absolute; inset: 0; width: 658px; height: 933px; }
  .brand {
    position: absolute; right: 14px; top: 28px; text-align: center;
    font-family: "Roboto", sans-serif; font-weight: 500; color: var(--ink);
    display: flex; align-items: center; gap: 6px;
  }
  .brand-mark { width: 10px; height: 10px; border-radius: 50%; background: var(--ink); }
  .brand-name { line-height: 1.05; }
  .brand-name .big { display: block; font-size: 17px; letter-spacing: 1px; }
  .brand-name .small { display: block; font-size: 9px; letter-spacing: 1px; }
  .kicker {
    position: absolute; left: 46px; top: 484px;
    font-size: 22px; font-style: italic; font-weight: 300; opacity: .85;
  }
  .headline {
    position: absolute; left: 44px; top: 522px;
    font-family: "Cinzel", serif; font-weight: 900; font-size: 50px;
    line-height: 56px; letter-spacing: 1px;
  }
  .pitch {
    position: absolute; left: 46px; top: 708px;
    font-size: 19.5px; line-height: 34px; letter-spacing: .3px;
  }
  .rule {
    position: absolute; left: 48px; top: 776px; width: 304px; height: 3px; background: var(--ink);
  }
  .rule::before {
    content: ""; position: absolute; left: -3px; top: -3px;
    width: 9px; height: 9px; border-radius: 50%; background: var(--ink);
  }
  .cta {
    position: absolute; left: 47px; top: 806px;
    display: flex; align-items: center; gap: 26px;
  }
  .cta-label { font-size: 26px; font-weight: 500; letter-spacing: 2px; }
  .cta-phone { display: flex; align-items: center; gap: 12px; font-size: 28px; font-weight: 500; letter-spacing: 2px; }
  .cta-phone svg { width: 32px; height: 38px; }
  .web {
    position: absolute; left: 0; right: 0; top: 890px;
    display: flex; justify-content: center; align-items: center; gap: 12px;
    font-size: 19px;
  }
  .web svg { width: 20px; height: 20px; }
</style>
</head>
<body>
  <main class="poster">
    <div class="hero-photo" role="img" aria-label="Photo of two young musicians talking in a recording studio beside a mixing desk and studio monitor"></div>

    <svg class="shapes" viewBox="0 0 658 933" aria-hidden="true">
      <path class="wave" d="M658,361 C600,378 520,420 510,490 C505,545 530,585 560,640 L658,812 Z" fill="var(--accent-wave)"/>
      <path class="corner" d="M0,746 L162,933 L0,933 Z" fill="var(--accent-corner)"/>
    </svg>

    <div class="brand">
      <span class="brand-mark"></span>
      <span class="brand-name"><span class="big">MERIDIAN</span><span class="small">SCHOOL OF MUSIC</span></span>
    </div>

    <p class="kicker">Start your career</p>
    <h1 class="headline">BECOME<br>A MENTOR<br>TODAY</h1>
    <p class="pitch">Turn your skills and passion for music into a career<br>Designed for Musicians, Artists, Producers &amp; Teachers</p>
    <div class="rule"></div>

    <div class="cta">
      <span class="cta-label">APPLY NOW</span>
      <span class="cta-phone">
        <svg viewBox="0 0 24 28" aria-hidden="true"><path d="M6 2 L10 2 L11 8 L8 10 C9 14 11 18 14 21 L17 19 L22 22 L21 26 C12 27 3 16 4 4 Z" fill="none" stroke="#fff" stroke-width="2" stroke-linejoin="round"/></svg>
        1300 482 816
      </span>
    </div>

    <div class="web">
      <svg viewBox="0 0 20 20" aria-hidden="true"><circle cx="10" cy="10" r="9" fill="#fff"/><path d="M5 6 C7 5 9 7 8 9 C7 11 5 10 4 12 M12 3 C11 6 14 7 15 9 C16 11 13 13 14 16" fill="none" stroke="#1a2e7a" stroke-width="1.8"/></svg>
      <span>www.meridianschoolofmusic.com.au</span>
    </div>
  </main>
</body>
</html>
```